Website customization using WordPress Theme already purchased

Need informational website for Orla Brightwell LLC. Orla Brightwell is investment group company for multiple cloud based products and website. We need website for anyone coming to our website to be able get information on our products. I already have WordPress theme that I would like to use. Right person/company will be able to customize WordPress theme to our needs and be able to give us final product of 7-9 pages of complete website.

Industry/Entity Type

Investment

Number of Pages Required

5+ page

Colors
add136
3176b5
ec1f27
f37122

```html
<!DOCTYPE html>
<html lang="en">
<head>
<meta charset="utf-8">
<title>Orla Brightwell Investment</title>
<link href="https://fonts.googleapis.com/css2?family=Raleway:wght@300;400;500;600;700;800&display=swap" rel="stylesheet">
<style>
:root{
  --red:#ec1f27;
  --blue:#3176b5;
  --deep-blue:#1d64ad;
  --orange:#f37122;
  --yellow:#f2e21d;
  --green:#add136;
  --ink:#222;
  --dark:#0d0d0d;
  --panel:#f2f2f2;
  --white:#fff;
}
*{box-sizing:border-box;margin:0;padding:0}
html,body{width:1200px;height:4293px;overflow:hidden}
body{font-family:"Raleway",sans-serif;color:var(--ink);background:var(--white);position:relative}
section,header,footer{position:absolute;left:0;width:1200px;overflow:hidden}
.abs{position:absolute}
.btn{position:absolute;display:flex;align-items:center;justify-content:center;font-family:"Raleway",sans-serif;font-size:19px;font-weight:500}
.btn-red{background:var(--red);color:var(--white)}
.btn-outline-red{border:2px solid var(--red);color:var(--white)}

/* top bar */
.topbar{top:0;height:34px;background:var(--white);font-size:11px}
.topbar .mail{left:138px;top:11px;display:flex;align-items:center;gap:6px}
.topbar .mail i{width:12px;height:8px;background:var(--red);display:block}
.nav{left:420px;top:8px;display:flex;gap:16px;font-size:13px}
.nav a{color:#333;text-decoration:none;padding-bottom:4px}
.nav a.active{color:var(--red);border-bottom:2px solid var(--red)}
.topbar .phone{left:958px;top:11px}

/* hero */
.hero{top:34px;height:706px}
.hero .photo{inset:0;position:absolute;background:radial-gradient(ellipse at 50% 35%,#6fb4ff 0%,#1c5fc7 35%,#0a2a6a 70%,#061436 100%)}
.hero .brand{left:0;width:1200px;top:168px;display:flex;justify-content:center;align-items:center;gap:10px;color:var(--white);font-weight:700;font-size:22px}
.hero .brand i{width:26px;height:26px;border-radius:50%;background:var(--white);display:block}
.hero h1{left:0;width:1200px;top:238px;text-align:center;color:var(--red);line-height:1}
.hero h1 .l1{display:block;font-size:66px;font-weight:700}
.hero h1 .l2{display:block;font-size:70px;font-weight:300;margin-top:4px}
.hero .lead{left:0;width:1200px;top:395px;text-align:center;color:var(--white);font-size:17px;font-weight:700;line-height:1.35}

/* about */
.about{top:740px;height:577px;background:#e9e9e9}
.about .box{left:135px;top:12px;width:925px;height:545px;background:#f7f7f7}
.title-red{color:var(--red);font-weight:700;font-size:62px;text-align:center;width:1200px;left:0}
.about p{left:138px;top:210px;width:555px;font-size:14px;line-height:1.65;color:#333}
.about .btn{left:135px;top:492px;width:176px;height:42px;border:2px solid var(--blue);color:#222;background:var(--white)}
.ph{position:absolute}

/* services */
.services{top:1317px;height:565px;background:linear-gradient(180deg,#2a2a2a,#151515)}
.services .intro{left:215px;top:128px;width:775px;text-align:center;color:var(--white);font-size:12.5px;line-height:1.7}
.svc{position:absolute;top:243px;width:250px;text-align:center;color:var(--white)}
.svc h3{color:var(--yellow);font-size:14px;font-weight:700;margin:10px 0 4px}
.svc p{font-size:11px;line-height:1.5}
.services .btn{left:511px;top:490px;width:178px;height:44px}

/* partners */
.partners{top:1882px;height:510px;background:var(--panel)}
.partners h2{left:135px;top:95px;color:var(--deep-blue);font-size:72px;font-weight:700;line-height:1.05}
.partners p{left:135px;top:340px;width:460px;font-size:13px;line-height:1.6;color:#333}
.grid{left:739px;top:106px;width:310px;display:grid;grid-template-columns:1fr 1fr;gap:3px}
.grid div{height:91px;border:2px solid var(--orange);background:var(--white);display:flex;align-items:center;justify-content:center}
.grid div span{width:90px;height:34px;background:#d9dde3;border-radius:4px;display:block}
.arrows{display:flex;gap:4px}
.arrows i{width:20px;height:20px;display:flex;align-items:center;justify-content:center}
.arrows i:first-child{background:var(--orange)}
.arrows i:last-child{background:#222}

/* award */
.award{top:2392px;height:492px;background:var(--dark)}
.award h2{left:135px;top:92px;color:var(--red);font-size:68px;font-weight:700;line-height:1.06}
.award p{left:135px;top:412px;width:860px;color:var(--white);font-size:12px;line-height:1.7}

/* blog */
.blog{top:2884px;height:725px;background:linear-gradient(180deg,#e6e6e6,#f4f4f4 40%,#eaeaea)}
.blog .circle{left:157px;top:323px;width:260px;height:260px;border-radius:50%}
.blog h3{left:467px;top:320px;font-size:29px;font-weight:700;color:#222}
.blog p{left:467px;top:368px;width:650px;font-size:12px;line-height:1.5;color:#333}
.blog .btn-red{left:467px;top:522px;width:150px;height:36px;font-size:17px}
.blog .arrows{position:absolute;left:990px;top:538px}
.blog .view{left:561px;top:636px;width:178px;height:44px;color:#222;border:2px solid var(--red);background:transparent}

/* contact */
.contact{top:3609px;height:644px;background:var(--dark)}
.contact h2{left:0;width:1200px;top:60px;text-align:center;color:var(--deep-blue);font-size:64px;font-weight:700}
.field{position:absolute;left:143px;width:502px;border-bottom:1px solid #bbb;color:var(--white);font-size:12px;padding-bottom:3px}
.contact .send{left:143px;top:518px;width:152px;height:38px;font-size:17px}
.contact .divider{left:750px;top:205px;width:1px;height:305px;background:#555}
.info{position:absolute;left:843px;display:flex;align-items:center;gap:16px;color:var(--white);font-size:13px;font-weight:600;line-height:1.4}
.info i{width:42px;height:42px;border-radius:50%;background:var(--red);display:flex;align-items:center;justify-content:center;flex:none}
.social{left:851px;top:464px;display:flex;gap:6px}
.social i{width:22px;height:22px;background:var(--white);display:block;border-radius:2px}
.social i.r{background:var(--red)}

footer{top:4253px;height:40px;background:var(--deep-blue);color:var(--white);font-size:13px;display:flex;align-items:center;justify-content:center}
</style>
</head>
<body>

<header class="topbar">
  <div class="abs mail"><i></i>info@orla-brightwell.com</div>
  <nav class="abs nav">
    <a class="active" href="#">Home</a><a href="#">About</a><a href="#">Services</a><a href="#">Case Studio</a><a href="#">Blog</a><a href="#">Contact</a>
  </nav>
  <div class="abs phone">&#9990; 0800-555-0142</div>
</header>

<section class="hero">
  <div class="photo" role="img" aria-label="Business team silhouettes in front of a blue stock market display"></div>
  <div class="abs brand"><i></i>Orla Brightwell</div>
  <h1 class="abs"><span class="l1">Orla Brightwell</span><span class="l2">Investment</span></h1>
  <p class="abs lead">We aim to help our customers to attain their strategic<br>goals through people.</p>
  <a class="btn btn-red" style="left:511px;top:458px;width:178px;height:44px">Contact Us</a>
</section>

<section class="about">
  <div class="abs box"></div>
  <h2 class="abs title-red" style="top:50px">How We Are</h2>
  <p class="abs">Lorem Ipsum is simply dummy text of the printing and typesetting industry. Lorem Ipsum has been the industry's standard dummy text ever since the 1500s, when an unknown printer took a galley of type and scrambled it to make a type specimen book. It has survived not only five centuries, but also the leap into electronic typesetting, remaining essentially unchanged. It was popularised in the 1960s with the release of Letraset sheets containing Lorem Ipsum passages, and more recently with desktop publishing software like Aldus PageMaker including versions of Lorem Ipsum.</p>
  <a class="btn">Contact Us</a>
  <div class="ph" style="left:773px;top:177px;width:287px;height:273px;background:linear-gradient(160deg,#fff 0%,#f7f0e0 45%,#f3c9c9 100%)" role="img" aria-label="Illustration of a businessman on a scooter riding up a rising red arrow"></div>
</section>

<section class="services">
  <h2 class="abs title-red" style="top:30px">Our Services</h2>
  <p class="abs intro">Lorem Ipsum is simply dummy text of the printing and typesetting industry. Lorem Ipsum has been the industry's standard dummy text ever since the 1500s, when an unknown printer took a galley of type and scrambled it to make a type specimen book. It has survived not only five centuries, but also the 1 sheets containing Lorem</p>
  <div class="svc" style="left:170px">
    <div class="ph" style="position:relative;margin:0 auto;width:70px;height:105px;background:linear-gradient(180deg,#3a3a4a,#222)" role="img" aria-label="Illustration of a trainer presenting"></div>
    <h3>Training &amp; Development</h3>
    <p>Lorem Ipsum is simply dummy text of the printing and typesetting industry. Lorem Ipsum has been the industry's standard dummy text ever since the 1500s, when an unknown printer</p>
  </div>
  <div class="svc" style="left:482px">
    <div class="ph" style="position:relative;margin:0 auto;width:100px;height:105px;background:linear-gradient(180deg,#3a3a3a,#1f6f7a)" role="img" aria-label="Illustration of a rising bar chart"></div>
    <h3>Talent Planning &amp; Acquisition</h3>
    <p>Lorem Ipsum is simply dummy text of the printing and typesetting industry. Lorem Ipsum has been the industry's standard dummy text ever since the 1500s, when an unknown printer</p>
  </div>
  <div class="svc" style="left:797px">
    <div class="ph" style="position:relative;margin:0 auto;width:100px;height:105px;background:linear-gradient(180deg,#3a3a3a,#c98a1e)" role="img" aria-label="Illustration of a megaphone"></div>
    <h3>Motivational Speakers.</h3>
    <p>Lorem Ipsum is simply dummy text of the printing and typesetting industry. Lorem Ipsum has been the industry's standard dummy text ever since the 1500s, when an unknown printer</p>
  </div>
  <a class="btn btn-outline-red">View All</a>
</section>

<section class="partners">
  <h2 class="abs">Who have<br>we worked<br>with?</h2>
  <p class="abs">Lorem Ipsum is simply dummy text of the printing and typesetting industry. Lorem Ipsum has been the industry's standard dummy text ever since the 1500s, when an unknown printer took a galley of type and scrambled it to make a type specimen book. It has survived not only five centuries, but also the 1 sheets containing Lorem</p>
  <div class="abs grid">
    <div><span></span></div><div><span></span></div>
    <div><span></span></div><div><span></span></div>
    <div><span></span></div><div><span></span></div>
  </div>
  <div class="abs arrows" style="left:875px;top:410px">
    <i><svg width="8" height="10"><path d="M7 1 2 5l5 4" stroke="#fff" stroke-width="2" fill="none"/></svg></i>
    <i><svg width="8" height="10"><path d="M1 1l5 4-5 4" stroke="#fff" stroke-width="2" fill="none"/></svg></i>
  </div>
</section>

<section class="award">
  <h2 class="abs">Best Human<br>Resouarces<br>Consultancy<br>Firm</h2>
  <div class="ph" style="left:710px;top:85px;width:355px;height:273px;background:linear-gradient(180deg,#e8b326 0%,#c88a12 55%,#2f6fb5 100%)" role="img" aria-label="Illustration of a hand holding a golden trophy"></div>
  <p class="abs">Lorem Ipsum is simply dummy text of the printing and typesetting industry. Lorem Ipsum has been the industry's standard dummy text ever since the 1500s, when an unknown printer took a galley of type and scrambled it to make a type specimen book. It has survived not only five centuries, but also the 1 sheets containing Lorem.</p>
</section>

<section class="blog">
  <h2 class="abs title-red" style="top:175px">Our Blog</h2>
  <div class="ph circle" style="background:radial-gradient(circle at 50% 40%,#4f8fe0,#123a80 70%)" role="img" aria-label="Silhouettes of a business team"></div>
  <h3 class="abs">How to train &amp; development</h3>
  <p class="abs">Lorem Ipsum is simply dummy text of the printing and typesetting industry. Lorem Ipsum has been the industry's standard dummy text ever since the 1500s, when an unknown printer took a galley of type and scrambled it to make a type specimen book. It has survived not only five centuries, but also the 1 sheets containing Lo.Lorem Ipsum is simply dummy text of the printing and typesetting industry. Lorem Ipsum has been the industry's standard dummy text ever since the 1500s, when an unknown printer took a galley of type and scrambled it to make a type specimen book. It has survived not only five centuries, but also the 1 sheets containing Loremlorem</p>
  <a class="btn btn-red">Read More</a>
  <div class="arrows">
    <i style="background:var(--red)"><svg width="8" height="10"><path d="M7 1 2 5l5 4" stroke="#fff" stroke-width="2" fill="none"/></svg></i>
    <i><svg width="8" height="10"><path d="M1 1l5 4-5 4" stroke="#fff" stroke-width="2" fill="none"/></svg></i>
  </div>
  <a class="btn view">View All</a>
</section>

<section class="contact">
  <h2 class="abs">Get in Touch</h2>
  <div class="field" style="top:186px">NAME :</div>
  <div class="field" style="top:258px">EMAIL :</div>
  <div class="field" style="top:330px">SUBJECT :</div>
  <div class="field" style="top:451px">MESSAGE :</div>
  <a class="btn btn-red send">Send</a>
  <div class="abs divider"></div>
  <div class="info" style="top:193px"><i><svg width="18" height="18" viewBox="0 0 24 24"><path fill="#fff" d="M6.6 10.8a15 15 0 0 0 6.6 6.6l2.2-2.2c.3-.3.7-.4 1-.2 1.1.4 2.3.6 3.6.6.6 0 1 .4 1 1V20c0 .6-.4 1-1 1A17 17 0 0 1 3 4c0-.6.4-1 1-1h3.5c.6 0 1 .4 1 1 0 1.3.2 2.5.6 3.6.1.3 0 .7-.2 1z"/></svg></i>0800-555-0142</div>
  <div class="info" style="top:274px"><i><svg width="18" height="14" viewBox="0 0 18 14"><rect x="1" y="1" width="16" height="12" fill="#fff"/><path d="M1 1l8 6 8-6" stroke="#ec1f27" stroke-width="1.5" fill="none"/></svg></i>info@orla-brightwell.com</div>
  <div class="info" style="top:357px"><i><svg width="14" height="20" viewBox="0 0 14 20"><path fill="#fff" d="M7 0a7 7 0 0 0-7 7c0 5 7 13 7 13s7-8 7-13a7 7 0 0 0-7-7zm0 9.5A2.5 2.5 0 1 1 7 4.5a2.5 2.5 0 0 1 0 5z"/></svg></i>24 Calle del Olmo Road,<br>28 4LK Madrid, Spain</div>
  <div class="abs social"><i></i><i></i><i class="r"></i><i></i><i></i></div>
</section>

<footer>Copyright © 2018 · orla-brightwell.com</footer>

</body>
</html>
```